Relaxation, deep tissue sports massage

We need an opening of anew massage centre poster
relaxation, deep tissue and sports massage
POSTER SIZE A4 and for a 1meter X 1meter stand
the business name is Toverin , we have a logo already , which i enclose
the poster needs to be eye catching
location Brindle Lane Medical Clinic 0872914658 for an appointment
location uHealth on Tarrowby 0873195246 for an appointment

Target Market(s)

public

Industry/Entity Type

Massage

Requirements
Must have
• logo , be vibrant ,eye catching and inviting
Nice to have
• massage picture , logo etc

```html
<!DOCTYPE html>
<html lang="en">
<head>
<meta charset="utf-8">
<title>Toverin Massage Centre – Opening Poster</title>
<link rel="stylesheet" href="https://fonts.googleapis.com/css2?family=Anton&family=Montserrat:wght@500;700&display=swap">
<style>
  :root {
    --stage: #000000;
    --skin-light: #f0c9b0;
    --skin-mid: #d9a285;
    --skin-deep: #b7775d;
    --lip: #c9645e;
    --rose: #b2506a;
    --rose-line: #f2a2bf;
    --glow: #ffd9a0;
    --band: rgba(255, 240, 235, 0.42);
    --ink: #111111;
  }
  * { margin: 0; padding: 0; box-sizing: border-box; }
  html, body {
    width: 1200px; height: 1200px; overflow: hidden;
    background: var(--stage);
  }
  .poster {
    position: absolute; left: 186px; top: 18px;
    width: 832px; height: 1162px; overflow: hidden;
    font-family: "Montserrat", sans-serif;
  }
  .poster__photo {
    position: absolute; inset: 0;
    background:
      radial-gradient(ellipse 55% 10% at 55% 64%, var(--lip) 0%, rgba(201,100,94,0) 100%),
      radial-gradient(ellipse 70% 60% at 50% 45%, var(--skin-light) 0%, var(--skin-mid) 60%, var(--skin-deep) 100%);
  }
  .spa-type {
    position: absolute; inset: 0; width: 832px; height: 1162px;
  }
  .spa-type text {
    font-family: "Anton", sans-serif;
    font-size: 470px;
    fill: rgba(255, 236, 225, 0.38);
    stroke: var(--rose-line);
    stroke-width: 5;
    filter: url(#glow);
  }
  .band {
    position: absolute; left: 0; width: 100%;
    background: var(--band);
  }
  .band--top {
    top: 48px; height: 98px;
    text-align: center; color: var(--rose);
  }
  .band__title {
    font-size: 43px; font-weight: 500; letter-spacing: 1px;
    padding-top: 4px; line-height: 52px;
  }
  .band__title strong { font-weight: 700; }
  .band__services {
    font-size: 23px; font-weight: 500; letter-spacing: 1px; word-spacing: 14px;
    line-height: 30px;
  }
  .band--bottom {
    top: 1024px; height: 96px; color: var(--ink);
  }
  .location { position: absolute; font-size: 17px; line-height: 20px; }
  .location__name { font-weight: 700; }
  .location__phone { font-weight: 500; }
  .location--first { left: 196px; top: 6px; }
  .location--second { left: 300px; top: 46px; }
  .brand-mark {
    position: absolute; right: 76px; top: 34px;
    display: flex; align-items: center; gap: 8px;
    font-size: 22px; font-weight: 500; color: #2e6b3a;
  }
  .brand-mark__dot {
    width: 14px; height: 14px; border-radius: 50%; background: #2e6b3a;
  }
</style>
</head>
<body>
  <main class="poster">
    <div class="poster__photo" role="img" aria-label="Close-up photograph of a relaxed woman with closed eyes and a gentle smile"></div>

    <svg class="spa-type" viewBox="0 0 832 1162" aria-hidden="true">
      <defs>
        <filter id="glow" x="-10%" y="-10%" width="120%" height="120%">
          <feGaussianBlur in="SourceAlpha" stdDeviation="6" result="blur"/>
          <feFlood flood-color="#ffd9a0" flood-opacity="0.8"/>
          <feComposite in2="blur" operator="in" result="glowColor"/>
          <feMerge><feMergeNode in="glowColor"/><feMergeNode in="SourceGraphic"/></feMerge>
        </filter>
      </defs>
      <text x="50" y="342" textLength="760" lengthAdjust="spacingAndGlyphs">SPA</text>
      <text x="50" y="762" textLength="760" lengthAdjust="spacingAndGlyphs">SPA</text>
      <text x="50" y="1182" textLength="760" lengthAdjust="spacingAndGlyphs">SPA</text>
    </svg>

    <header class="band band--top">
      <h1 class="band__title"><strong>TOVERIN</strong> MASSAGE CENTRE</h1>
      <p class="band__services">RELAXATION DEEP&nbsp;TISSUE SPORTS&nbsp;MASSAGE</p>
    </header>

    <footer class="band band--bottom">
      <div class="location location--first">
        <p class="location__name">BRINDLE LANE MEDICAL CLINIC</p>
        <p class="location__phone">0872914658 FOR AN APPOINTMENT</p>
      </div>
      <div class="location location--second">
        <p class="location__name">uHEALTH ON TARROWBY</p>
        <p class="location__phone">0873195246 FOR AN APPOINTMENT</p>
      </div>
      <div class="brand-mark">
        <span>Toverin massage</span>
        <span class="brand-mark__dot"></span>
      </div>
    </footer>
  </main>
</body>
</html>
```